Global Beard Oil Review Business needs a refresh

topwhiskertonic.net is a global business who's mission is to curate all available beard oils from around the world, review and grade them and present this curated collection to the user of the website.

The scope of this job includes the web site design and the design of a suitable logo to be used in the site header.

The existing site can be seen on http://topwhiskertonic.net, however this is a mock-up only the style and logo should NOT be used. This is to give you an idea of the concept of the site only.

This job is for PSD design only.

See attached design brief for detailed design requirements.
Updates

Project Deadline Extended
Reason: Extending deadline by 5 days to allow for final submissions

Target Market(s)

Men's grooming / retail

Industry/Entity Type

Retail

Number of Pages Required

2 page

Font styles to use
Sans Serif

Requirements
Must have
• 1) Comparison Table
• 2) Side Bar
• 3) Header area
• 4) Photo of Calvin Dorrow (attached - can be circular or "cut-out")
• 5) Cool beard-oriented custom design background (e.g., stylistic black/brown on brown/orange beard background. I envision this beard background "drawing" rather than photo based)
• (see attached design requirements for details)
Nice to have
• Signature style writing at top with name "Calvin Dorrow"
Should not have
• Do NOT use the look & feel or logo from the existing site.

```html
<!DOCTYPE html>
<html lang="en">
<head>
<meta charset="utf-8">
<title>Top Whisker Tonic – The World's #1 Beard Oil Authority</title>
<link href="https://fonts.googleapis.com/css2?family=Lato:wght@400;700;900&family=Kaushan+Script&display=swap" rel="stylesheet">
<style>
:root{
  --orange:#f7941d;
  --ink:#222;
  --head:#8c8c8c;
  --row-alt:#a8a8a8;
  --white:#fff;
}
*{box-sizing:border-box;margin:0;padding:0}
html,body{width:1200px;height:802px;overflow:hidden}
body{position:relative;font-family:"Lato",sans-serif;color:var(--ink);background:#7a7a7a}
.wood{position:absolute;inset:0;background:linear-gradient(90deg,#8d8d8d 0%,#6e6e6e 12%,#9a9a9a 25%,#777 38%,#8f8f8f 52%,#6c6c6c 66%,#959595 80%,#747474 100%)}
.header{position:absolute;left:0;top:0;width:1200px;height:222px;background:linear-gradient(180deg,#3a3a3a,#2a2a2a)}
.brand{position:absolute;left:0;width:1200px;top:70px;text-align:center;font-weight:900;font-size:26px;color:var(--orange);letter-spacing:1px}
.brand-dot{display:inline-block;width:14px;height:14px;border-radius:50%;background:var(--orange);margin-right:8px;vertical-align:2px}
.nav a{position:absolute;top:180px;font-weight:700;font-variant:small-caps;font-size:20px;color:var(--white);text-decoration:none;line-height:24px}
.nav a.active{color:var(--orange)}
.nav a.active::after{content:"";position:absolute;left:0;right:0;top:38px;height:2px;background:var(--orange)}
.nav a.hover{color:var(--orange)}
.main{position:absolute;left:239px;top:258px;width:526px;height:380px;background:rgba(235,235,235,.93);padding:0 9px}
.main h1{margin-top:18px;font-size:24px;font-weight:900;color:#222}
.main p{margin-top:5px;font-size:11px;line-height:18.6px;color:#222}
.compare{margin-top:5px;width:510px;border-collapse:collapse;table-layout:fixed;font-size:7.5px}
.compare th{background:var(--head);height:42px;font-weight:700;font-size:8.5px;color:#333;text-align:left;padding:0 2px;line-height:12px}
.compare td{height:42.5px;padding:0 2px;color:#222;line-height:9.5px}
.compare tr:nth-child(even) td{background:var(--row-alt)}
.compare .num,.compare th.num{text-align:center}
.bottle{display:block;margin:0 auto;width:10px;height:30px;border-radius:2px 2px 3px 3px;background:linear-gradient(#3a2a18,#8a5a20)}
.bottle.small{width:8px;height:22px;background:#222}
.buy{display:inline-block;background:var(--orange);color:#fff;font-size:6px;font-weight:700;padding:6px 4px;white-space:nowrap}
.side{position:absolute;left:775px;width:184px;background:rgba(50,50,50,.92);color:#fff}
.profile{top:258px;height:155px;text-align:center}
.avatar{position:absolute;left:46px;top:14px;width:91px;height:91px;border-radius:50%;background:radial-gradient(circle at 50% 40%,#bbb,#444)}
.profile .title{position:absolute;top:115px;width:100%;font-size:11px;font-weight:700}
.profile .sig{position:absolute;top:131px;width:100%;font-size:11px}
.profile .sig span{font-family:"Kaushan Script",cursive}
.popular{top:422px;height:216px;padding:6px 4px 0 13px;overflow:hidden}
.popular h3{font-size:11px;font-weight:700;display:flex;align-items:center;gap:5px;padding-bottom:5px;margin-right:12px;border-bottom:2px solid #ddd}
.bolt{width:16px;height:16px;background:var(--orange);display:inline-flex;align-items:center;justify-content:center}
.post{display:flex;gap:5px;padding:9px 0 3px;margin-right:12px;border-bottom:1px solid #888;height:59px}
.post:last-of-type{border:none}
.thumb{flex:none;width:48px;height:47px;background:linear-gradient(135deg,#8a6a3a,#4a3a22)}
.post-text{width:120px;margin-right:-12px}
.post h4{font-size:7.6px;font-weight:900;line-height:10px;text-transform:uppercase;white-space:nowrap;letter-spacing:-.1px}
.post .meta{font-size:7.5px;line-height:13.5px;color:#ddd;white-space:nowrap}
.post .meta b{font-weight:400;color:var(--orange)}
.ico{display:inline-block;width:6px;height:6px;background:#ddd;margin-right:5px;vertical-align:0}
.ico.user{border-radius:50% 50% 1px 1px}
.footer{position:absolute;left:0;top:674px;width:1200px;height:128px;background:#2a2a2a;color:#fff}
.footer h5{font-variant:small-caps;font-weight:700;font-size:12px;text-decoration:underline;text-underline-offset:3px}
.quick{position:absolute;left:239px;top:18px}
.quick h5{font-size:14px;margin-bottom:6px}
.quick a{display:block;color:#fff;text-decoration:none;font-size:9px;line-height:15px}
.news{position:absolute;left:537px;top:18px;width:140px}
.news p{margin-top:6px;font-size:8.5px;line-height:10.5px}
.news .field{margin-top:10px;width:126px;height:17px;border:1px solid #ddd;font-size:8.5px;color:#bbb;padding:2px 7px}
.news .submit{margin-top:8px;width:57px;height:18px;background:var(--orange);font-size:6px;text-align:center;line-height:18px}
.follow{position:absolute;right:242px;top:14px;text-align:right}
.icons{margin-top:8px;display:flex;gap:6px;justify-content:flex-end}
.icons span{width:19px;height:19px;background:var(--orange);border-radius:2px}
</style>
</head>
<body>
<div class="wood" role="img" aria-label="Grey weathered wooden planks background"></div>

<header class="header">
  <div class="brand"><span class="brand-dot"></span>Top Whisker Tonic</div>
  <nav class="nav">
    <a class="active" style="left:328px">Home</a>
    <a style="left:414px">Review Methodology</a>
    <a class="hover" style="left:613px">Charter</a>
    <a style="left:718px">Blog</a>
    <a style="left:798px">About Me</a>
  </nav>
</header>

<main class="main">
  <h1>The World’s #1 Beard Oil Authority</h1>
  <p>Here is the master list of beard oils reviewed to date. You can link directly to the corresponding review by clicking on the name of the beard oil. In accordance with our charter, we are actively working to locate and review every single beard oil available on the planet Earth, so check back regularly for updates.</p>
  <table class="compare">
    <colgroup><col style="width:58px"><col style="width:58px"><col style="width:27px"><col style="width:50px"><col style="width:42px"><col style="width:37px"><col style="width:45px"><col style="width:48px"><col style="width:38px"><col style="width:45px"><col style="width:62px"></colgroup>
    <thead><tr><th style="padding-left:15px">Suplier</th><th>Name</th><th>Oil</th><th>Country of Origin</th><th class="num">Aroma</th><th class="num">Grease</th><th class="num">Condition</th><th class="num">Delivery</th><th class="num">Value</th><th class="num">Overallt</th><th class="num">Link</th></tr></thead>
    <tbody>
      <tr><td style="padding-left:13px">Northfold Beard Co.</td><td>Timberline</td><td><span class="bottle" role="img" aria-label="Timberline oil bottle"></span></td><td>Australia</td><td class="num">7</td><td class="num">5</td><td class="num">3</td><td class="num">5</td><td class="num">6</td><td class="num">7</td><td class="num"><span class="buy">GET YOURS NOW</span></td></tr>
      <tr><td style="padding-left:13px">Pappy Wren Grooming</td><td>Misty Ridge Man Beard Oil</td><td><span class="bottle" role="img" aria-label="Misty Ridge oil bottle"></span></td><td>Australia</td><td class="num">8</td><td class="num">8</td><td class="num">8</td><td class="num">8</td><td class="num">6</td><td class="num">8</td><td class="num"><span class="buy">GET YOURS NOW</span></td></tr>
      <tr><td style="padding-left:13px">Bristled Rogue</td><td>Forester</td><td><span class="bottle" role="img" aria-label="Forester oil bottle" style="background:linear-gradient(#ddd,#c8904a)"></span></td><td>USA</td><td class="num">7</td><td class="num">5</td><td class="num">1</td><td class="num">5</td><td class="num">3</td><td class="num">6</td><td class="num"><span class="buy">GET YOURS NOW</span></td></tr>
      <tr><td style="padding-left:13px">Barrowman Men's Grooming</td><td>Barrowman Beard Oil</td><td><span class="bottle small" role="img" aria-label="Barrowman oil bottle"></span></td><td>Australia</td><td class="num">7</td><td class="num">3</td><td class="num">7</td><td class="num">8</td><td class="num">10</td><td class="num">8</td><td class="num"><span class="buy">GET YOURS NOW</span></td></tr>
      <tr><td style="padding-left:13px">Evenbody Soaps</td><td>Outbacker's Beard Oil</td><td><span class="bottle small" role="img" aria-label="Outbacker's oil bottle"></span></td><td>Australia</td><td class="num">7</td><td class="num">5</td><td class="num">8</td><td class="num">8</td><td class="num">5</td><td class="num">7</td><td class="num"><span class="buy">GET YOURS NOW</span></td></tr>
    </tbody>
  </table>
</main>

<aside class="side profile">
  <div class="avatar" role="img" aria-label="Circular portrait photo of Calvin Dorrow"></div>
  <div class="title">Global Beard Oil Reviews</div>
  <div class="sig">- by <span>Calvin Dorrow</span></div>
</aside>

<aside class="side popular">
  <h3><span class="bolt"><svg width="8" height="12" viewBox="0 0 8 12"><path d="M5 0L0 7h3l-1 5 6-8H5z" fill="#2a2a2a"/></svg></span>Popular Posts</h3>
  <div class="post"><div class="thumb" role="img" aria-label="Photo of beard oil bottle"></div><div class="post-text"><h4>Misty Ridge Man<br>Beard Oil Pappy ...</h4><div class="meta"><span class="ico user"></span>BY: <b>Calvin Dorrow</b><br><span class="ico"></span>February 12, 2016</div></div></div>
  <div class="post"><div class="thumb" role="img" aria-label="Photo of beard oil bottle outdoors" style="background:linear-gradient(135deg,#4a5a3a,#2a2a22)"></div><div class="post-text"><h4>Outbacker's Face/Beard<br>Oil by Evenbody ...</h4><div class="meta"><span class="ico user"></span>BY: <b>Calvin Dorrow</b><br><span class="ico"></span>February 09, 2016</div></div></div>
  <div class="post"><div class="thumb" role="img" aria-label="Photo of beard oil bottle" style="background:linear-gradient(135deg,#c8b890,#6a5a3a)"></div><div class="post-text"><h4>Barrowman Beard Oil<br>by Barrowman ...</h4><div class="meta"><span class="ico user"></span>BY: <b>Calvin Dorrow</b><br><span class="ico"></span>January 25, 2016</div></div></div>
</aside>

<footer class="footer">
  <div class="quick"><h5>Quick Links</h5><a>Home</a><a>Review Methedology</a><a>Charter</a><a>Blog</a><a>About Me</a></div>
  <div class="news"><h5>Subscribe to my newsletter</h5><p>Don't miss out on any of my reviews and offers.</p><div class="field">Enter your email here</div><div class="submit">SUBMIT</div></div>
  <div class="follow"><h5>Follow me on</h5><div class="icons"><span></span><span></span><span></span></div></div>
</footer>
</body>
</html>
```